Quick Order Banner Design

We want to build a banner that will sit in the middle of the page that will replace our current quick order banner that we don't like. See https://www.snapvellum.com/image/48230917?key=3f91ac2de7b4c8e05a6d1f29b73e4c0a

Text:
Quick Order is a fast and easy way to fill your cart with items when you know exactly what you want to purchase.

Design ideas:

Use foto Noto Sans. Color codes can be of #00539E, FDBC38, #6AC07A

We don't want a computer screen in banner nor a person. You can look at our competitors below for ideas.

i don't like the design here https://tovirapartsdepot.com/blog/post/order-parts-fast-with-our-new-quick-order-feature but the concept is cool as it shows where to access it.. but i want other ideas too.

Our staging server is plimdex4.com

Our competitors:
https://www.halvorsupplyco.com/
https://www.lumbrix.com/
https://www.vosko.com/
https://www.quelt.com/index.html

Target Market(s)

B2B, Contractors who buy our products

Industry/Entity Type

hvac

Requirements
Should not have
• people photos or computer or computer screens.

```html
<!DOCTYPE html>
<html lang="en">
<head>
<meta charset="utf-8">
<title>Quick Order Banner</title>
<link rel="stylesheet" href="https://fonts.googleapis.com/css2?family=Noto+Sans:wght@400;600;700&display=swap">
<style>
:root{
  --page:#e3e4e6;
  --blue:#00539e;
  --blue-deep:#073a7c;
  --gold:#fdbc38;
  --white:#ffffff;
  --ink:#3a3a3a;
  --muted:#8a8a8a;
  --line:#e2e2e2;
  --side:#6e6f71;
  --btn-dark:#4a4d52;
  --orange:#f07d1a;
  --product:#8a5a3a;
}
*{box-sizing:border-box;margin:0;padding:0}
html,body{width:1200px;height:636px;overflow:hidden;background:var(--page);font-family:"Noto Sans",sans-serif}
.banner{position:absolute;left:36px;top:151px;width:1130px;height:322px;
  background:linear-gradient(90deg,var(--blue) 0%,#0a4f99 45%,var(--blue-deep) 100%);
  box-shadow:4px 6px 8px rgba(0,0,0,.35);overflow:hidden}
.backdrop-mark{position:absolute;left:40px;top:0;width:230px;height:322px;
  background:radial-gradient(circle at 50% 45%,rgba(255,255,255,.07),rgba(255,255,255,0) 70%)}
.headline{position:absolute;left:35px;top:52px;color:var(--gold);font-size:64px;font-weight:700;line-height:1;letter-spacing:.5px;white-space:nowrap}
.subline{position:absolute;left:38px;top:123px;color:var(--white);font-size:35px;font-weight:700;line-height:44px;white-space:nowrap}
.cta{position:absolute;left:39px;top:241px;width:202px;height:39px;background:var(--white);
  color:var(--blue);font-size:24px;font-weight:700;display:flex;align-items:center;justify-content:center;padding-right:14px}

.order-tool{position:absolute;left:631px;top:20px;width:444px;height:280px;background:var(--white);color:var(--ink)}
.order-tool *{position:absolute}
.tool-title{left:7px;top:3px;font-size:12px;font-weight:700;color:#444}
.tool-intro{left:7px;top:24px;font-size:4.3px;color:#555;white-space:nowrap}
.table-frame{left:7px;top:53px;width:327px;height:226px;border:1px solid var(--line);border-bottom:none}
.col-head{top:62px;font-size:5px;font-weight:700;color:#333}
.row-line{left:8px;width:326px;height:1px;background:var(--line)}
.sku-field{left:12px;width:162px;height:15px;border:1px solid #cfcfcf;border-radius:2px;font-size:4.5px;color:#555;padding:4px 0 0 4px}
.product-photo{width:12px;height:20px;background:var(--product);border-radius:1px}
.step{width:15px;height:15px;background:var(--btn-dark);color:#fff;font-size:9px;font-weight:700;display:flex;align-items:center;justify-content:center;line-height:1}
.qty{font-size:5px;color:#444;width:10px;text-align:center}
.price{left:283px;font-size:4.5px;color:#444}
.trash{left:320px;width:6px;height:7px}
.add-rows{left:14px;top:225px;font-size:4.5px;color:var(--blue)}
.subtotal{left:253px;top:239px;font-size:5px;font-weight:700;color:#333}
.add-cart{left:253px;top:254px;width:55px;height:15px;background:var(--blue);color:#fff;font-size:5px;font-weight:700;display:flex;align-items:center;justify-content:center}

.bulk-panel{left:334px;top:53px;width:104px;height:224px;background:var(--side);color:#fff}
.panel-title{left:20px;font-size:5.5px;font-weight:700}
.panel-icon{left:7px;width:8px;height:9px}
.drop-zone{left:7px;top:22px;width:90px;height:57px;border:1px dashed #c8c8c8}
.drop-text{left:6px;top:6px;width:78px;font-size:4.3px;line-height:6px;text-align:center;color:#f0f0f0}
.choose-file{left:17px;top:32px;width:56px;height:10px;background:var(--blue);font-size:4.5px;font-weight:700;display:flex;align-items:center;justify-content:center}
.sample-link{left:0;top:46px;width:90px;text-align:center;font-size:4.3px;text-decoration:underline}
.tutorial{left:24px;top:94px;width:56px;height:11px;background:var(--orange);font-size:4.5px;font-weight:700;display:flex;align-items:center;justify-content:center}
.panel-rule{left:7px;top:112px;width:90px;height:1px;background:#8d8e90}
.paste-text{left:7px;top:133px;width:92px;font-size:4.3px;line-height:6px;text-align:center;color:#f0f0f0}
.paste-box{left:7px;top:159px;width:91px;height:44px;background:#fff;color:#444;font-size:4.3px;line-height:6px;padding:3px 4px}
.paste-box span{position:static;display:block}
.paste-submit{left:7px;top:207px;width:91px;height:10px;background:var(--blue);font-size:4.5px;font-weight:700;display:flex;align-items:center;justify-content:center}
</style>
</head>
<body>
<section class="banner">
  <div class="backdrop-mark" role="img" aria-label="Faint large snowflake emblem decoration"></div>
  <h1 class="headline">Quick Order</h1>
  <p class="subline">Our fast, efficient, easy-to-use<br>tool makes ordering simple.</p>
  <a class="cta">Try Now</a>

  <div class="order-tool">
    <h2 class="tool-title">Quick Order</h2>
    <p class="tool-intro">Quick Order is the fastest and easiest way to place your orders online. You can use the single item search below to enter product name / SKU or use the bulk csv import option.</p>

    <div class="table-frame"></div>
    <span class="col-head" style="left:14px">Product Name / SKU</span>
    <span class="col-head" style="left:186px">Photo</span>
    <span class="col-head" style="left:239px">Qty</span>
    <span class="col-head" style="left:283px">Price</span>

    <div class="row-line" style="top:74px"></div>
    <div class="sku-field" style="top:84px">Veltara, KRM40T118</div>
    <div class="product-photo" style="left:189px;top:81px" role="img" aria-label="Product photo"></div>
    <div class="step" style="left:218px;top:84px">−</div><span class="qty" style="left:235px;top:88px">1</span><div class="step" style="left:254px;top:84px">+</div>
    <span class="price" style="top:88px">$2,415.00</span>
    <svg class="trash" style="top:88px" viewBox="0 0 6 7"><rect x="1" y="1.5" width="4" height="5.5" fill="#555"/><rect x="0" y="0.5" width="6" height="1" fill="#555"/></svg>

    <div class="row-line" style="top:106px"></div>
    <div class="sku-field" style="top:116px">Veltara, DPL22C604</div>
    <div class="product-photo" style="left:190px;top:113px" role="img" aria-label="Product photo"></div>
    <div class="step" style="left:218px;top:116px">−</div><span class="qty" style="left:235px;top:120px">1</span><div class="step" style="left:254px;top:116px">+</div>
    <span class="price" style="top:120px">$1,870.00</span>
    <svg class="trash" style="top:120px" viewBox="0 0 6 7"><rect x="1" y="1.5" width="4" height="5.5" fill="#555"/><rect x="0" y="0.5" width="6" height="1" fill="#555"/></svg>

    <div class="row-line" style="top:140px"></div>
    <div class="sku-field" style="top:145px">Enter Product Name or SKU to Add</div>
    <div class="step" style="left:218px;top:145px">−</div><div class="step" style="left:254px;top:145px">+</div>
    <span class="price" style="top:149px">$0.00</span>
    <svg class="trash" style="top:149px" viewBox="0 0 6 7"><rect x="1" y="1.5" width="4" height="5.5" fill="#555"/><rect x="0" y="0.5" width="6" height="1" fill="#555"/></svg>

    <div class="row-line" style="top:166px"></div>
    <div class="sku-field" style="top:171px">Enter Product Name or SKU to Add</div>
    <div class="step" style="left:218px;top:171px">−</div><div class="step" style="left:254px;top:171px">+</div>
    <span class="price" style="top:175px">$0.00</span>
    <svg class="trash" style="top:175px" viewBox="0 0 6 7"><rect x="1" y="1.5" width="4" height="5.5" fill="#555"/><rect x="0" y="0.5" width="6" height="1" fill="#555"/></svg>

    <div class="row-line" style="top:192px"></div>
    <div class="sku-field" style="top:196px">Enter Product Name or SKU to Add</div>
    <div class="step" style="left:218px;top:196px">−</div><div class="step" style="left:254px;top:196px">+</div>
    <span class="price" style="top:200px">$0.00</span>
    <svg class="trash" style="top:200px" viewBox="0 0 6 7"><rect x="1" y="1.5" width="4" height="5.5" fill="#555"/><rect x="0" y="0.5" width="6" height="1" fill="#555"/></svg>
    <div class="row-line" style="top:216px"></div>

    <span class="add-rows">+ Add Additional Rows</span>
    <span class="subtotal">Subtotal: $4,480.00</span>
    <div class="add-cart">Add To Cart</div>

    <div class="bulk-panel">
      <svg class="panel-icon" style="top:8px" viewBox="0 0 8 9"><rect x="0.5" y="0.5" width="7" height="8" rx="1" fill="none" stroke="#fff"/><rect x="2" y="3" width="4" height="1" fill="#fff"/><rect x="2" y="5" width="4" height="1" fill="#fff"/></svg>
      <span class="panel-title" style="top:8px">Import Your Order</span>
      <div class="drop-zone">
        <p class="drop-text">Drag and drop a .CSV file here, or select file from your computer to import to cart.</p>
        <div class="choose-file">Choose File</div>
        <span class="sample-link">Download Sample CSV</span>
      </div>
      <div class="tutorial">ⓘ Tutorial</div>
      <div class="panel-rule"></div>
      <svg class="panel-icon" style="top:118px" viewBox="0 0 8 9"><rect x="0.5" y="0.5" width="7" height="8" rx="1" fill="#fff"/></svg>
      <span class="panel-title" style="top:118px">Paste Your Order</span>
      <p class="paste-text">Copy and paste or manually enter your order with the SKU # and quantity, separated by a comma on each line.</p>
      <div class="paste-box"><span>Example:</span><span>&nbsp;</span><span>HXN517302,1</span><span>QT-58319042270,2</span></div>
      <div class="paste-submit">Add to Cart</div>
    </div>
  </div>
</section>
</body>
</html>
```